High-end b2b furniture company needs informational/photo brochure

Please note CHANGE IN SIZE: 11 x 25.5 overall size, tri-fold brochure. Use lots of photos and must have a high-end, clean look because we are in the interior design industry. Designer must review our website to get an idea of branding! (www.halvorquist.example).

Instructions on where all photos/images should be placed are written as the file name for the jpgs/pdfs. Please ask if file name placement instructions are not clear!

There are extra images attached to use if needed, but you do not need to use all of these. There are also several images marked for the cover, but again, no need to use all of these if it looks too crowded. This will depend upon your design. (We would prefer a relatively clean, uncrowded look.)

Thank you for your hard work. I just increased the budget for first place on this project due to the large size of this brief.

Target Market(s)

Interior designers, architects, commercial property managers, shopping mall/retail managers. We sell commercial furniture ONLY (we do not sell to end consumers and we typically do not sell furniture for the home).

Industry/Entity Type

It Company

Font styles to use
Serif
Sans Serif
Other font styles liked:
• Prefer mostly sans serif, but can use serif if design calls for it. We use variations of Gil Sans MT in much of our marketing. Can use a decorative or script font for accent, but nothing that looks "old fashioned" and no cursive or anything that looks "curly."

Colors
cadf82
add136
faa54b
f78f20
ffffff

Requirements
Must have
• An upscale feel that appeals to high-end interior designers. Photography needs to be fairly large to highlight the furniture. (Text can be placed around furniture)
Nice to have
• Ample white and dark (black or charcoal gray) space
Should not have
• No old fashioned/cursive fonts. No shadows behind photos or shadows behind text boxes. Since furniture design is our business, do not cut off the lines of our furniture designs by overlapping text or images.

```html
<!DOCTYPE html>
<html lang="en">
<head>
<meta charset="utf-8">
<title>Halvorquist Furniture — Presentation Folder</title>
<link rel="stylesheet" href="https://fonts.googleapis.com/css2?family=Lato:wght@300;400&family=Roboto+Condensed:wght@400;700&family=Titillium+Web:wght@400;600;700&display=swap">
<style>
  :root {
    --lime: #c3d021;
    --olive: #76901f;
    --leaf: #5e7a12;
    --ink: #1c1c1c;
    --charcoal: #2b2b2b;
    --paper: #ffffff;
    --backdrop: #ececec;
    --text-muted: #555555;
  }
  * { margin: 0; padding: 0; box-sizing: border-box; }
  html, body { width: 1200px; height: 1200px; overflow: hidden; }
  body { background: var(--backdrop); position: relative; font-family: "Titillium Web", sans-serif; }

  .spread { position: absolute; left: 120px; top: 280px; width: 960px; height: 640px; display: flex; }
  .panel { position: relative; width: 480px; height: 640px; background: var(--paper); overflow: hidden; }

  .base-rule { position: absolute; left: 0; right: 0; top: 590px; height: 5px; background: var(--charcoal); }
  .base-band { position: absolute; left: 0; right: 0; top: 595px; bottom: 0; background: var(--olive); }

  /* back panel */
  .back-mark { position: absolute; left: 55px; top: 440px; width: 96px; height: 96px; background: var(--lime); }
  .contact { position: absolute; left: 168px; top: 470px; }
  .contact-title { font-weight: 700; font-size: 13px; color: var(--leaf); letter-spacing: .3px; text-transform: uppercase; margin-bottom: 6px; }
  .contact-line { font-size: 11px; color: var(--ink); display: flex; align-items: center; gap: 5px; line-height: 18px; }
  .contact-line svg { width: 8px; height: 8px; }
  .address { position: absolute; left: 340px; top: 510px; font-size: 10.5px; color: var(--ink); line-height: 15px; }
  .address .contact-line { font-size: 10.5px; line-height: 15px; }

  /* front panel */
  .brand-square { position: absolute; left: 14px; top: 20px; width: 80px; height: 72px; background: var(--lime); z-index: 2; }
  .brand { position: absolute; left: 112px; top: 34px; }
  .brand-name { font-family: "Lato", sans-serif; font-weight: 300; font-size: 15px; letter-spacing: 10px; color: var(--charcoal); text-transform: uppercase; }
  .brand-tag { font-family: "Lato", sans-serif; font-weight: 400; font-size: 10px; letter-spacing: 3px; color: var(--lime); text-align: right; margin-top: 4px; padding-right: 6px; }

  .photo { position: absolute; }
  .photo-hero { left: 0; top: 72px; width: 480px; height: 178px; background: linear-gradient(180deg, #4a3f38 0%, #3d3834 45%, #6f78c8 70%, #8a8fd6 100%); }
  .photo-row { position: absolute; left: 0; top: 250px; width: 480px; height: 132px; background: var(--olive); }
  .photo-lounge { left: 0; top: 6px; width: 156px; height: 120px; background: linear-gradient(160deg, #8b6a52, #c9b6a2 60%, #6e5a4d); }
  .photo-fireside { left: 162px; top: 6px; width: 156px; height: 120px; background: linear-gradient(160deg, #3b3a36, #6d5d48 55%, #b88d57); }
  .photo-lobby { left: 324px; top: 6px; width: 156px; height: 120px; background: linear-gradient(160deg, #c7a36f, #5b5a63 55%, #3a3a44); }

  .headline { position: absolute; left: 28px; top: 400px; font-family: "Roboto Condensed", sans-serif; line-height: 1; }
  .headline-top { display: flex; align-items: flex-end; }
  .word-doesnt { font-size: 50px; font-weight: 400; color: var(--ink); letter-spacing: 1px; }
  .word-just { margin-left: 8px; background: var(--lime); color: var(--paper); font-size: 46px; font-weight: 700; padding: 2px 60px 0 8px; }
  .headline-bottom { margin-top: 4px; white-space: nowrap; }
  .word-manufacture { font-size: 32px; font-weight: 700; color: var(--olive); }
  .word-products { font-size: 32px; font-weight: 700; color: var(--ink); margin-left: 6px; }
</style>
</head>
<body>
  <main class="spread">
    <section class="panel panel-back">
      <div class="back-mark" aria-hidden="true"></div>
      <div class="contact">
        <h2 class="contact-title">Contact Info</h2>
        <p class="contact-line"><svg viewBox="0 0 10 10"><rect x="1" y="2" width="8" height="6" fill="none" stroke="#76901f" stroke-width="1.4"/></svg>customerservice@halvorquist.example</p>
        <p class="contact-line"><svg viewBox="0 0 10 10"><circle cx="5" cy="5" r="3.6" fill="none" stroke="#76901f" stroke-width="1.4"/></svg>www.halvorquist.example</p>
      </div>
      <address class="address" style="font-style:normal">
        418 Alder Row, Suite 12<br>
        Brightwater, WA 99000
        <p class="contact-line"><svg viewBox="0 0 10 10"><path d="M2 1 L4 1 L4.6 3 L3.4 4 Q4.5 6 6 6.6 L7 5.4 L9 6 L9 8 Q4 9 1 2 Z" fill="#76901f"/></svg>(555) 014-2200</p>
        <p class="contact-line"><svg viewBox="0 0 10 10"><rect x="1" y="3" width="8" height="5" fill="none" stroke="#76901f" stroke-width="1.4"/><rect x="3" y="1" width="4" height="2" fill="#76901f"/></svg>(555) 014-2201</p>
      </address>
      <div class="base-rule"></div>
      <div class="base-band"></div>
    </section>

    <section class="panel panel-front">
      <div class="brand-square" aria-hidden="true"></div>
      <div class="brand">
        <p class="brand-name">Halvorquist</p>
        <p class="brand-tag">furniture</p>
      </div>
      <div class="photo photo-hero" role="img" aria-label="Showroom with a large blue sectional sofa beneath framed wall art"></div>
      <div class="photo-row">
        <div class="photo photo-lounge" role="img" aria-label="Lounge with a beige sectional and red artwork"></div>
        <div class="photo photo-fireside" role="img" aria-label="Fireside seating area with a wooden coffee table"></div>
        <div class="photo photo-lobby" role="img" aria-label="Hotel lobby with patterned armchairs"></div>
      </div>
      <h1 class="headline">
        <span class="headline-top"><span class="word-doesnt">DOESN’T</span><span class="word-just">JUST</span></span>
        <span class="headline-bottom" style="display:block"><span class="word-manufacture">MANUFACTURE</span><span class="word-products">PRODUCTS</span></span>
      </h1>
      <div class="base-rule"></div>
      <div class="base-band"></div>
    </section>
  </main>
</body>
</html>
```